Business Image

I have recently had a new company logo made up and require some new business cards to go with it.

Target Market(s)

Developers & high worth clients.

Industry/Entity Type

Business

Contact Information for Business Card

The business is in the construction/management industry. It needs to be classy but have a industrial feel. I would like the business card to be a elegant presentation in itself.

Requirements
Must have
• Current logo & company name. Colouring needs to be the same as the current design also.
Nice to have
• A few different designs & presentations of single and double sided business cards.

```html
<!DOCTYPE html>
<html lang="en">
<head>
<meta charset="utf-8">
<title>Keystone Build Group — Business Cards</title>
<link href="https://fonts.googleapis.com/css2?family=Roboto:wght@400;500;700&family=Roboto+Condensed:wght@700&display=swap" rel="stylesheet">
<style>
  :root {
    --backdrop: #2b2c2e;
    --card-light: #f6f6f4;
    --card-dark: #232425;
    --brand-blue: #265a8c;
    --accent-blue: #3a7dc0;
    --ink-gray: #555759;
    --ink-white: #f2f2f2;
    --divider: #8a8c8e;
  }
  * { margin: 0; padding: 0; box-sizing: border-box; }
  html, body { width: 1200px; height: 900px; overflow: hidden; }
  body {
    background: var(--backdrop);
    font-family: "Roboto", Arial, sans-serif;
    position: relative;
  }
  .card {
    position: absolute;
    left: 290px;
    width: 620px;
    height: 354px;
    border-radius: 3px;
    box-shadow: 0 10px 26px rgba(0,0,0,0.45);
  }
  .card-front { top: 70px; background: var(--card-light); }
  .card-back  { top: 476px; background: var(--card-dark); }

  /* Front */
  .brand {
    position: absolute;
    top: 92px; left: 0; right: 0;
    display: flex; flex-direction: column; align-items: center;
  }
  .brand-square {
    width: 46px; height: 46px;
    background: var(--brand-blue);
    margin-bottom: 18px;
  }
  .brand-name {
    color: var(--brand-blue);
    font-weight: 700;
    font-size: 34px;
    letter-spacing: 3px;
    text-align: center;
    line-height: 1.15;
    text-transform: uppercase;
  }
  .brand-url {
    position: absolute;
    bottom: 46px; left: 0; right: 0;
    text-align: center;
    font-size: 15px;
    letter-spacing: 2.2px;
    color: var(--ink-gray);
  }

  /* Back */
  .identity {
    position: absolute;
    top: 96px; right: 348px;
    text-align: right;
  }
  .person-name {
    font-family: "Roboto Condensed", "Arial Narrow", sans-serif;
    font-weight: 700;
    font-size: 34px;
    color: var(--accent-blue);
    line-height: 1;
  }
  .person-role {
    margin-top: 8px;
    font-weight: 500;
    font-size: 17px;
    color: var(--ink-white);
  }
  .divider {
    position: absolute;
    left: 290px; top: 78px;
    width: 2px; height: 130px;
    background: linear-gradient(to bottom, transparent, var(--divider) 30%, var(--divider) 70%, transparent);
  }
  .contact-list {
    position: absolute;
    left: 314px; top: 84px;
    list-style: none;
  }
  .contact-item {
    display: flex; align-items: center;
    height: 23px;
    font-size: 16px;
    color: var(--ink-white);
  }
  .contact-icon {
    width: 16px; height: 16px;
    margin-right: 10px;
    fill: var(--accent-blue);
    flex: none;
  }
  .address {
    position: absolute;
    left: 0; right: 0; bottom: 62px;
    display: flex; justify-content: center; align-items: center;
    font-size: 17px;
    color: var(--ink-white);
  }
  .address .contact-icon { margin-right: 6px; }
</style>
</head>
<body>

  <section class="card card-front">
    <div class="brand">
      <div class="brand-square"></div>
      <div class="brand-name">Keystone<br>Build Group</div>
    </div>
    <p class="brand-url">www.keystonebuildgroup.com</p>
  </section>

  <section class="card card-back">
    <div class="identity">
      <h1 class="person-name">DANIEL HARLOW</h1>
      <p class="person-role">CEO/FOUNDER</p>
    </div>
    <div class="divider"></div>
    <ul class="contact-list">
      <li class="contact-item">
        <svg class="contact-icon" viewBox="0 0 16 16"><path d="M3.5 1.5l2.5-.5 1.5 3.5-1.8 1.2c.8 1.8 2.2 3.2 4 4l1.2-1.8 3.5 1.5-.5 2.5c-.3 1-1.3 1.6-2.3 1.4C6.5 12.4 3.6 9.5 2.1 4.4c-.2-1 .4-2.6 1.4-2.9z"/></svg>
        555.210.4417
      </li>
      <li class="contact-item">
        <svg class="contact-icon" viewBox="0 0 16 16"><path d="M4.5 0h7c.8 0 1.5.7 1.5 1.5v13c0 .8-.7 1.5-1.5 1.5h-7C3.7 16 3 15.3 3 14.5v-13C3 .7 3.7 0 4.5 0zM4.8 2v10.5h6.4V2zM8 13.3a.9.9 0 100 1.8.9.9 0 000-1.8z"/></svg>
        555.381.7629
      </li>
      <li class="contact-item">
        <svg class="contact-icon" viewBox="0 0 16 16"><path d="M4 1h8v4H4zM1.5 6h13c.8 0 1.5.7 1.5 1.5V12h-3v3H3v-3H0V7.5C0 6.7.7 6 1.5 6zM4.5 10v3.5h7V10z"/></svg>
        555.946.0283
      </li>
      <li class="contact-item">
        <svg class="contact-icon" viewBox="0 0 16 16"><path d="M1 3h14v1.2L8 8.8 1 4.2zM1 5.8l7 4.6 7-4.6V13H1z"/></svg>
        daniel@keystone.com
      </li>
      <li class="contact-item">
        <svg class="contact-icon" viewBox="0 0 16 16"><circle cx="8" cy="8" r="7"/><path d="M1 8h14M8 1c2.4 2 2.4 12 0 14M8 1C5.6 3 5.6 13 8 15" stroke="#232425" stroke-width="1" fill="none"/></svg>
        www.keystone.com
      </li>
    </ul>
    <p class="address">
      <svg class="contact-icon" viewBox="0 0 16 16"><path d="M8 0a5.5 5.5 0 00-5.5 5.5C2.5 10 8 16 8 16s5.5-6 5.5-10.5A5.5 5.5 0 008 0zm0 3.3a2.2 2.2 0 110 4.4 2.2 2.2 0 010-4.4z"/></svg>
      2916 Cedar Ridge Road, Juneau, Alaska 99801
    </p>
  </section>

</body>
</html>
```